Promotional Ad/Flyer - Kavo Leasing

A division of our company, Kavo Leasing (kavo-leasing.example) is celebrating its 1-year anniversary in September and we would like to run a promotion. I am looking to have a promotional ad/flyer made-up for email mailings and LinkedIn posts and possibly have on our site. Have plenty of product photos to share if needed, not a prerequisite to use our product in the ad but open to it. Can also be cool graphics as well. We want to capture the viewers attention with the 30 DAYS FREE! The message is simple:
We are celebrating our 1-Year Anniversary by offering a Special Peak-Season Promotion!

FREE RENTALS for 30 days with a minimum 30-Day rental!

Valid from Sep. 1 - Dec. 31 & while supplies last.

Please contact our sales department for more details.

Email: quotes@kavo-leasing.example
Phone: +1-555-284-9317

```html
<!DOCTYPE html>
<html lang="en">
<head>
<meta charset="utf-8">
<title>Kavo Leasing – 1 Year Anniversary Promotion Options</title>
<link href="https://fonts.googleapis.com/css2?family=Anton&family=Crimson+Pro:ital,wght@0,700;1,600&family=Open+Sans:wght@400;600;700;800&display=swap" rel="stylesheet">
<style>
  :root {
    --board: #ffffff;
    --night-top: #1b0d06;
    --night-mid: #140c1e;
    --night-low: #1c1408;
    --gold: #e4b530;
    --gold-light: #f6d77a;
    --gold-deep: #9c6f12;
    --label-gold: #a8801c;
    --orange: #ff6a00;
    --ink: #000000;
    --white: #ffffff;
    --band-blue: #3355b8;
    --brand-blue: #2c4696;
    --ribbon-red: #8e1414;
  }
  * { box-sizing: border-box; margin: 0; padding: 0; }
  html, body { width: 1200px; height: 584px; overflow: hidden; background: var(--board); }
  body { position: relative; font-family: "Open Sans", Arial, sans-serif; }

  .option { position: absolute; top: 57px; width: 340px; }
  .option--one { left: 49px; }
  .option--two { left: 432px; }
  .option--three { left: 815px; }

  .option-label {
    position: absolute; top: 459px; left: 0; width: 340px; text-align: center;
    font-family: "Open Sans", Arial, sans-serif; font-weight: 400; font-size: 27px;
    color: var(--label-gold); letter-spacing: 0.5px;
  }

  .flyer { position: relative; width: 340px; height: 440px; overflow: hidden; background: var(--night-top); }

  .flyer-backdrop {
    position: absolute; inset: 0;
    background:
      radial-gradient(ellipse 70% 22% at 50% 60%, rgba(240,180,40,0.75), rgba(200,130,20,0.35) 55%, rgba(0,0,0,0) 100%),
      radial-gradient(ellipse 60% 14% at 50% 78%, rgba(230,170,40,0.55), rgba(0,0,0,0) 100%),
      linear-gradient(180deg, var(--night-top) 0%, var(--night-mid) 30%, #1d1208 55%, var(--night-low) 100%);
  }

  .emblem-art {
    position: absolute; left: 95px; top: 42px; width: 150px; height: 140px; border-radius: 50%;
    background: radial-gradient(circle, rgba(214,160,40,0.28) 0%, rgba(160,110,20,0.18) 55%, rgba(0,0,0,0) 72%);
  }

  .celebrate-arc { position: absolute; left: 0; top: 0; width: 340px; height: 130px; }
  .celebrate-arc text {
    font-family: "Crimson Pro", Georgia, serif; font-weight: 700; font-size: 13px;
    fill: var(--white); letter-spacing: 1px;
  }

  .emblem-one {
    position: absolute; left: 0; width: 340px; top: 46px; text-align: center;
    font-family: "Crimson Pro", Georgia, serif; font-weight: 700; font-size: 72px; line-height: 1;
    color: var(--gold); text-shadow: 1px 2px 0 var(--gold-deep);
  }
  .emblem-year {
    position: absolute; left: 0; width: 340px; top: 115px; text-align: center;
    font-family: "Crimson Pro", Georgia, serif; font-weight: 700; font-size: 16px; line-height: 1;
    color: var(--gold); letter-spacing: 0.5px;
  }
  .emblem-ribbon {
    position: absolute; left: 118px; width: 104px; top: 134px; height: 17px; border-radius: 9px;
    background: var(--ribbon-red); text-align: center;
    font-family: "Open Sans", Arial, sans-serif; font-weight: 400; font-size: 10px; line-height: 17px;
    color: var(--gold-light); letter-spacing: 0.4px;
  }

  .lead-in {
    position: absolute; left: 0; width: 340px; top: 170px; text-align: center;
    font-family: "Crimson Pro", Georgia, serif; font-style: italic; font-weight: 600; font-size: 14px;
    color: var(--white);
  }
  .promo-title {
    position: absolute; left: 0; width: 340px; top: 188px; text-align: center;
    font-family: "Crimson Pro", Georgia, serif; font-weight: 700; font-size: 19px;
    color: var(--white); text-shadow: 1px 1px 2px #000;
  }
  .headline {
    position: absolute; left: 0; width: 340px; top: 216px; text-align: center;
    font-family: "Anton", Impact, sans-serif; font-size: 55px; line-height: 1; letter-spacing: -0.5px;
    color: var(--gold); text-shadow: 2px 3px 0 #2a1c06, -1px -1px 0 var(--gold-light);
  }

  .offer-bar {
    position: absolute; left: 36px; width: 268px; top: 281px; height: 18px;
    background: var(--orange); color: var(--white); text-align: center;
    font-weight: 700; font-size: 8.6px; line-height: 18px;
  }
  .validity-frame {
    position: absolute; left: 36px; width: 268px; top: 299px; height: 33px;
    border: 1px solid var(--orange); border-top: none;
  }
  .validity {
    position: absolute; left: 69px; width: 203px; top: 303px; height: 19px;
    background: var(--ink); color: var(--white); text-align: center;
    font-weight: 700; font-size: 13px; line-height: 19px;
  }
  .validity em { font-style: normal; color: var(--orange); }
  .supplies {
    position: absolute; left: 116px; width: 110px; top: 325px; height: 13px;
    background: var(--ink); color: var(--white); text-align: center;
    font-weight: 700; font-size: 8.4px; line-height: 13px;
  }

  .brand-stage { position: absolute; left: 0; top: 340px; width: 340px; height: 62px; }
  .brand-stage path { fill: var(--white); }

  .brand {
    position: absolute; left: 0; width: 340px; top: 360px; height: 28px;
    display: flex; align-items: center; justify-content: center; gap: 8px;
  }
  .brand-square { width: 16px; height: 16px; background: var(--white); }
  .brand-name { font-weight: 800; font-size: 21px; color: var(--white); line-height: 1; }
  .flyer--light-brand .brand-square { background: var(--brand-blue); }
  .flyer--light-brand .brand-name { color: var(--brand-blue); }

  .contact-band { position: absolute; left: 0; top: 401px; width: 340px; height: 39px; background: var(--band-blue); }
  .contact-cta {
    position: absolute; left: 36px; width: 268px; top: 393px; height: 17px;
    background: var(--orange); color: var(--white); text-align: center;
    font-weight: 700; font-size: 7.2px; line-height: 17px;
  }
  .contact-line {
    position: absolute; left: 0; width: 340px; top: 415px; height: 12px;
    display: flex; align-items: center; justify-content: center; gap: 6px;
    color: var(--white); font-weight: 600; font-size: 7.3px; white-space: nowrap;
  }
  .contact-item { display: inline-flex; align-items: center; gap: 2px; }
  .contact-item svg { width: 7px; height: 7px; }
  .contact-item svg * { fill: none; stroke: var(--white); stroke-width: 1.2; }
  .contact-sep { width: 1px; height: 8px; background: var(--orange); }
</style>
</head>
<body>

<!-- Option 1 -->
<section class="option option--one">
  <article class="flyer">
    <div class="flyer-backdrop" role="img" aria-label="Dark night background with glowing gold bokeh sparkles"></div>
    <div class="emblem-art" role="img" aria-label="Gold laurel wreath anniversary emblem with red ribbon"></div>
    <svg class="celebrate-arc" viewBox="0 0 340 130" aria-hidden="true">
      <defs><path id="arc-one" d="M 92 78 A 84 84 0 0 1 248 78"/></defs>
      <text><textPath href="#arc-one" startOffset="50%" text-anchor="middle">WE ARE CELEBRATING OUR</textPath></text>
    </svg>
    <div class="emblem-one">1</div>
    <div class="emblem-year">YEAR</div>
    <div class="emblem-ribbon">ANNIVERSARY</div>
    <p class="lead-in">by offering a</p>
    <h2 class="promo-title">Special Peak-Season Promotion!</h2>
    <h1 class="headline">30 DAYS FREE!</h1>
    <p class="offer-bar">FREE RENTALS for 30 days with a minimum 30-Day rental!</p>
    <div class="validity-frame"></div>
    <p class="validity">VALID FROM <em>SEP. 1 - DEC. 31</em></p>
    <p class="supplies">WHILE SUPPLIES LAST.</p>
    <div class="brand"><span class="brand-square"></span><span class="brand-name">Kavo Leasing</span></div>
    <div class="contact-band"></div>
    <p class="contact-cta">PLEASE CONTACT OUR SALES DEPARTMENT FOR MORE DETAILS.</p>
    <div class="contact-line">
      <span class="contact-item"><svg viewBox="0 0 8 8"><rect x="0.6" y="1.5" width="6.8" height="5"/><path d="M0.6 1.5 L4 4.5 L7.4 1.5"/></svg>quotes@kavo-leasing.example</span>
      <span class="contact-sep"></span>
      <span class="contact-item"><svg viewBox="0 0 8 8"><circle cx="4" cy="4" r="3.4"/><path d="M2.8 2.4 L3.4 2.2 L3.8 3.2 L3.4 3.6 Q4 4.8 4.6 4.6 L5 4.3 L5.8 4.9 L5.4 5.6 Q3 5.6 2.6 2.8 Z"/></svg>+1-555-284-9317</span>
      <span class="contact-sep"></span>
      <span class="contact-item"><svg viewBox="0 0 8 8"><circle cx="4" cy="4" r="3.4"/><ellipse cx="4" cy="4" rx="1.5" ry="3.4"/><path d="M0.6 4 H7.4"/></svg>kavo-leasing.example</span>
    </div>
  </article>
  <p class="option-label">OPTION - 1</p>
</section>

<!-- Option 2 -->
<section class="option option--two">
  <article class="flyer flyer--light-brand">
    <div class="flyer-backdrop" role="img" aria-label="Dark night background with glowing gold bokeh sparkles"></div>
    <div class="emblem-art" role="img" aria-label="Gold laurel wreath anniversary emblem with red ribbon"></div>
    <svg class="celebrate-arc" viewBox="0 0 340 130" aria-hidden="true">
      <defs><path id="arc-two" d="M 92 78 A 84 84 0 0 1 248 78"/></defs>
      <text><textPath href="#arc-two" startOffset="50%" text-anchor="middle">WE ARE CELEBRATING OUR</textPath></text>
    </svg>
    <div class="emblem-one">1</div>
    <div class="emblem-year">YEAR</div>
    <div class="emblem-ribbon">ANNIVERSARY</div>
    <p class="lead-in">by offering a</p>
    <h2 class="promo-title">Special Peak-Season Promotion!</h2>
    <h1 class="headline">30 DAYS FREE!</h1>
    <p class="offer-bar">FREE RENTALS for 30 days with a minimum 30-Day rental!</p>
    <div class="validity-frame"></div>
    <p class="validity">VALID FROM <em>SEP. 1 - DEC. 31</em></p>
    <p class="supplies">WHILE SUPPLIES LAST.</p>
    <svg class="brand-stage" viewBox="0 0 340 62" aria-hidden="true">
      <path d="M57 62 L76 18 Q81 10 90 10 L250 10 Q259 10 264 18 L283 62 Z"/>
    </svg>
    <div class="brand"><span class="brand-square"></span><span class="brand-name">Kavo Leasing</span></div>
    <div class="contact-band"></div>
    <p class="contact-cta">PLEASE CONTACT OUR SALES DEPARTMENT FOR MORE DETAILS.</p>
    <div class="contact-line">
      <span class="contact-item"><svg viewBox="0 0 8 8"><rect x="0.6" y="1.5" width="6.8" height="5"/><path d="M0.6 1.5 L4 4.5 L7.4 1.5"/></svg>quotes@kavo-leasing.example</span>
      <span class="contact-sep"></span>
      <span class="contact-item"><svg viewBox="0 0 8 8"><circle cx="4" cy="4" r="3.4"/><path d="M2.8 2.4 L3.4 2.2 L3.8 3.2 L3.4 3.6 Q4 4.8 4.6 4.6 L5 4.3 L5.8 4.9 L5.4 5.6 Q3 5.6 2.6 2.8 Z"/></svg>+1-555-284-9317</span>
      <span class="contact-sep"></span>
      <span class="contact-item"><svg viewBox="0 0 8 8"><circle cx="4" cy="4" r="3.4"/><ellipse cx="4" cy="4" rx="1.5" ry="3.4"/><path d="M0.6 4 H7.4"/></svg>kavo-leasing.example</span>
    </div>
  </article>
  <p class="option-label">OPTION - 2</p>
</section>

<!-- Option 3 -->
<section class="option option--three">
  <article class="flyer flyer--light-brand">
    <div class="flyer-backdrop" role="img" aria-label="Dark night background with glowing gold bokeh sparkles"></div>
    <div class="emblem-art" role="img" aria-label="Gold laurel wreath anniversary emblem with red ribbon"></div>
    <svg class="celebrate-arc" viewBox="0 0 340 130" aria-hidden="true">
      <defs><path id="arc-three" d="M 92 78 A 84 84 0 0 1 248 78"/></defs>
      <text><textPath href="#arc-three" startOffset="50%" text-anchor="middle">WE ARE CELEBRATING OUR</textPath></text>
    </svg>
    <div class="emblem-one">1</div>
    <div class="emblem-year">YEAR</div>
    <div class="emblem-ribbon">ANNIVERSARY</div>
    <p class="lead-in">by offering a</p>
    <h2 class="promo-title">Special Peak-Season Promotion!</h2>
    <h1 class="headline">30 DAYS FREE!</h1>
    <p class="offer-bar">FREE RENTALS for 30 days with a minimum 30-Day rental!</p>
    <div class="validity-frame"></div>
    <p class="validity">VALID FROM <em>SEP. 1 - DEC. 31</em></p>
    <p class="supplies">WHILE SUPPLIES LAST.</p>
    <svg class="brand-stage" viewBox="0 0 340 62" aria-hidden="true">
      <path d="M0 25 Q170 -15 340 25 L340 62 L0 62 Z"/>
    </svg>
    <div class="brand"><span class="brand-square"></span><span class="brand-name">Kavo Leasing</span></div>
    <div class="contact-band"></div>
    <p class="contact-cta">PLEASE CONTACT OUR SALES DEPARTMENT FOR MORE DETAILS.</p>
    <div class="contact-line">
      <span class="contact-item"><svg viewBox="0 0 8 8"><rect x="0.6" y="1.5" width="6.8" height="5"/><path d="M0.6 1.5 L4 4.5 L7.4 1.5"/></svg>quotes@kavo-leasing.example</span>
      <span class="contact-sep"></span>
      <span class="contact-item"><svg viewBox="0 0 8 8"><circle cx="4" cy="4" r="3.4"/><path d="M2.8 2.4 L3.4 2.2 L3.8 3.2 L3.4 3.6 Q4 4.8 4.6 4.6 L5 4.3 L5.8 4.9 L5.4 5.6 Q3 5.6 2.6 2.8 Z"/></svg>+1-555-284-9317</span>
      <span class="contact-sep"></span>
      <span class="contact-item"><svg viewBox="0 0 8 8"><circle cx="4" cy="4" r="3.4"/><ellipse cx="4" cy="4" rx="1.5" ry="3.4"/><path d="M0.6 4 H7.4"/></svg>kavo-leasing.example</span>
    </div>
  </article>
  <p class="option-label">OPTION - 3</p>
</section>

</body>
</html>
```